Executive retreat/workshop flyer for Harbor Pathway

Our company, Harbor Pathway, runs intensive week long residential retreats for executives suffering from burnout syndrome. We have a programme of therapy which will enable clients to get clarity on what they want out of life and how to achieve it.

Our website is www.harborpathway-example.com. The flyer should have a consistent look and feel to the website. The flyer should be suitable for electronic distribution as well as printing.

The copy should read:

What is it all for? (IN BIG BOLD FONT)

We invite you to The Harbor Pathway

Discover a more meaningful way of being in this world and put passion and purpose back into your life.

Our leading experts will guide you through a holistic program of intellectual, physical, emotional, spiritual and financial work.

You will:

- Draw up a vision of how you want to live your life
- Understand negative behavior loops and how to manage them
- Rebalance relationships which have suffered from stress and neglect
- Examine your attitudes towards money through the Quadrafold System
- Access practical advice on how to implement your goals

Please join us in the beautiful Castlereagh Peninsula this August for a life-changing journey.

This is an intensive program custom tailored to your individual needs. We can only take on a very limited number of participants to maintain intimacy and quality of attention. Book early to avoid disappointment.

Details:

date - mon 27 August - sat 1 sept 2012

Venue- kestrelwood Eco retreat, stony ford, Australia, 1 hour from Melbourne

Price- Special launch offer of US$ 13,860 which is a 30% discount off the normal price of US$ 19,800

10% of profits go to charity

All accommodation, food and individual consultations included.

Please email info@harborpathway-example.com or contact Marnie at 6031 2946

Target Market(s)

Senior executives and leaders mostly with a financial background.

Industry/Entity Type

Residential

Requirements
Must have
• The brochure should look clear in electronic and print format. Can use photos which I've attached.
Nice to have
• Should have a warm, serene feel but appear professional and reliable.

```html
<!DOCTYPE html>
<html lang="en">
<head>
<meta charset="utf-8">
<title>The Harbor Pathway – Executive Retreat</title>
<link rel="stylesheet" href="https://fonts.googleapis.com/css2?family=Nunito:wght@900&family=Open+Sans:ital,wght@0,400;0,600;1,400&display=swap">
<style>
  :root {
    --purple: #5b2a86;
    --purple-deep: #3d1760;
    --panel: rgba(82, 28, 128, 0.86);
    --gold: #a8903f;
    --white: #ffffff;
    --flower-light: #f3ec58;
    --flower-mid: #d9d22a;
    --leaf: #8a9a3a;
  }
  * { margin: 0; padding: 0; box-sizing: border-box; }
  html, body { width: 848px; height: 1200px; overflow: hidden; background: #fff; }
  .flyer {
    position: relative;
    width: 848px;
    height: 1200px;
    overflow: hidden;
    font-family: "Open Sans", Arial, sans-serif;
    color: var(--white);
  }
  .flower-photo {
    position: absolute;
    inset: 0;
    background:
      radial-gradient(ellipse 280px 220px at 80% 45%, rgba(255,250,140,0.9), transparent 70%),
      radial-gradient(ellipse 260px 260px at 10% 80%, rgba(240,232,70,0.85), transparent 70%),
      radial-gradient(ellipse 300px 200px at 60% 95%, rgba(150,165,60,0.8), transparent 70%),
      radial-gradient(ellipse 240px 240px at 20% 30%, rgba(235,225,60,0.9), transparent 70%),
      linear-gradient(160deg, var(--flower-light) 0%, var(--flower-mid) 45%, var(--leaf) 100%);
  }
  .header-curve { position: absolute; top: 0; left: 0; width: 848px; height: 250px; }
  .brand {
    position: absolute;
    top: 74px;
    left: 0;
    width: 848px;
    text-align: center;
  }
  .brand-dot {
    display: block;
    width: 58px;
    height: 58px;
    margin: 0 auto 14px;
    border-radius: 50%;
    background: var(--purple);
  }
  .brand-name {
    font-family: "Open Sans", Arial, sans-serif;
    font-weight: 400;
    font-size: 32px;
    letter-spacing: 1px;
    color: var(--gold);
  }
  .headline {
    position: absolute;
    top: 268px;
    left: 0;
    width: 848px;
    text-align: center;
    font-family: "Nunito", Arial, sans-serif;
    font-weight: 900;
    font-size: 90px;
    line-height: 1;
    color: var(--white);
    -webkit-text-stroke: 6px var(--purple);
    paint-order: stroke fill;
    letter-spacing: -0.5px;
  }
  .info-panel {
    position: absolute;
    top: 394px;
    left: 58px;
    width: 734px;
    height: 692px;
    background: var(--panel);
    padding: 22px 34px 0 30px;
  }
  .invite {
    font-style: italic;
    font-size: 28px;
    text-align: center;
    margin-bottom: 22px;
    font-weight: 400;
  }
  .intro p, .benefits li { font-size: 15.5px; line-height: 1.35; }
  .intro p { margin-bottom: 14px; }
  .benefits { list-style: none; margin: 0 0 14px; }
  .details { margin-top: 16px; width: 420px; }
  .details p { font-size: 13.2px; line-height: 1.32; margin-bottom: 9px; }
  .site-url {
    position: absolute;
    top: 1114px;
    left: 0;
    width: 848px;
    text-align: center;
    font-family: "Nunito", Arial, sans-serif;
    font-weight: 900;
    font-size: 38px;
    color: var(--white);
    -webkit-text-stroke: 4px var(--purple);
    paint-order: stroke fill;
  }
</style>
</head>
<body>
<main class="flyer">
  <div class="flower-photo" role="img" aria-label="Close-up photograph of yellow flowering plants with a bee on a blossom"></div>

  <svg class="header-curve" viewBox="0 0 848 250" aria-hidden="true">
    <path d="M0 0 H848 V0 C800 150 620 242 420 242 C220 242 70 210 0 178 Z" fill="#ffffff"/>
    <path d="M0 178 C70 210 220 242 420 242 C620 242 800 150 848 0" fill="none" stroke="#5b2a86" stroke-width="4"/>
    <path d="M0 186 C70 218 220 249 420 249 C620 249 805 155 848 6" fill="none" stroke="#a8903f" stroke-width="3"/>
  </svg>

  <header class="brand">
    <span class="brand-dot" aria-hidden="true"></span>
    <span class="brand-name">The Harbor Pathway</span>
  </header>

  <h1 class="headline">What is it all for?</h1>

  <section class="info-panel">
    <h2 class="invite">We invite you to The Harbor Pathway</h2>
    <div class="intro">
      <p>Discover a more meaningful way of being in this world and put passion and purpose back into your life.</p>
      <p>Our leading experts will guide you through a holistic program of intellectual, physical, emotional, spiritual and financial work.</p>
      <p>You will:</p>
    </div>
    <ul class="benefits">
      <li>- Draw up a vision of how you want to live your life.</li>
      <li>- Understand negative behavior loops and how to manage them.</li>
      <li>- Rebalance relationships which have suffered from stress and neglect.</li>
      <li>- Examine your attitudes towards money through the Quadrafold System.</li>
      <li>- Access practical advice on how to implement your goals.</li>
    </ul>
    <div class="intro">
      <p>Please join us in the beautiful Castlereagh Peninsula this August for a life-changing journey.</p>
      <p>This is an intensive program custom tailored to your individual needs. We can only take on a very limited number of participants to maintain intimacy and quality of attention. Book early to avoid disappointment.</p>
    </div>
    <div class="details">
      <p>Date - mon 27 august - sat 1 september 2012.</p>
      <p>Venue - kestrelwood Eco retreat, stony ford, Australia, 1 hour from Melbourne.</p>
      <p>Price - Special launch offer of US$ 13,860 which is a 30% discount off the normal price of US$ 19,800.</p>
      <p>10% of profits go to charity.</p>
      <p>All accommodation, food and individual consultations included.</p>
      <p>Please email info@harborpathway-example.com or contact Marnie at 6031 2946</p>
    </div>
  </section>

  <p class="site-url">www.harborpathway-example.com</p>
</main>
</body>
</html>
```